Design new RK Capital business card 2016

We need a new business card for our company RK Capital Stewardship. We are a niche Alternative Investment Fund Manager based in Chester, in the North West of the UK.We market our services to global institutions such as banks, insurance companies, pension funds, etc. as well as wealthy individuals. Our main markets are Europe (Germany\France\Switzerland), the US and parts of Asia.
The design needs to be in line with existing company branding. Life the assets we deal with, the business card might suggest, "niche\alternative" type of attributes - however, it needs to remain professional, clean and appropriate for our client base.
Our existing business card format with relevant factual information is included, along with logo and branding details.

Target Market(s)

We market our services to global institutions such as banks, insurance companies, pension funds, etc. as well as wealthy individuals.

Industry/Entity Type

Financial Service

Contact Information for Business Card

please see attached pdf for information on existing business card which we should aim to convey on your new design. However:
- the wording "RK Capital Stewardship Ltd is Authorised and Regulated
by the Monetary Oversight Bureau. Registered No. 7139604" should be replaced with , "RK Capital Stewardship Ltd is an Alternative Investment Fund Manager Authorised and Regulated by the Monetary Oversight Bureau. Registered No. 7139604"
- the "reception" word on reverse can be omitted.
- the "retail: www.marbowhill.co.uk" wording can be omitted.
- the QR code is not required in the new version.

Font styles to use
Serif
Sans Serif

Requirements
Must have
• information on current business card, subject to comments provided above.
Nice to have
• Use of areas of solid colour instead of large areas of white space might be nice to experiment with. However, still need to have the general look and feel of the brand as presented on our website www.rkcapfold.co.uk
• If we had space for 3 bullet points describing what we do\who we are, this might be good to try out. e.g. alternative investment fund manager, longevity specialist, founded 1990.
• Also, we have a new tag line, "wisdom built to endure" which might fit nicely somewhere on the business card.
Should not have
• - no QR code
• - should not use all the colours in our logo as it looks very garish! Using one or two colours with black\white etc, seems to work better.

```html
<!DOCTYPE html>
<html lang="en">
<head>
<meta charset="utf-8">
<title>RK Capital Stewardship – Business Card</title>
<link rel="stylesheet" href="https://fonts.googleapis.com/css2?family=Arimo:wght@400;700&display=swap">
<style>
  :root {
    --canvas: #e9e7e2;
    --olive: #b19e12;
    --olive-light: #c9b52a;
    --brown: #6e3b08;
    --white: #ffffff;
    --ink: #6b3a10;
    --card-w: 720px;
    --card-h: 411px;
  }
  * { box-sizing: border-box; margin: 0; padding: 0; }
  html, body {
    width: 1200px; height: 950px; overflow: hidden;
    background: var(--canvas);
    font-family: "Arimo", Arial, sans-serif;
  }
  .sheet {
    width: 1200px; height: 950px;
    display: flex; flex-direction: column; align-items: center; justify-content: center;
    gap: 40px;
  }
  .card {
    width: var(--card-w); height: var(--card-h);
    box-shadow: 0 6px 18px rgba(0,0,0,.18);
    position: relative; overflow: hidden;
  }

  /* Front */
  .card-front {
    background: var(--olive);
    color: var(--white);
    display: flex; flex-direction: column; align-items: center;
    padding-top: 92px;
  }
  .brand-front {
    display: flex; align-items: center; gap: 14px;
    font-size: 34px; font-weight: 400; color: var(--white);
    letter-spacing: .5px;
  }
  .brand-dot { width: 22px; height: 22px; border-radius: 50%; background: var(--white); }
  .services {
    margin-top: 92px;
    font-size: 16px; letter-spacing: .3px;
  }
  .rule { width: 470px; height: 1px; background: var(--white); margin: 10px 0 12px; }
  .regulatory {
    font-size: 13px; line-height: 1.45; text-align: center; letter-spacing: .2px;
  }

  /* Back */
  .card-back { display: flex; background: var(--white); }
  .contact-panel {
    width: 47%; background: var(--brown); color: var(--white);
    padding: 118px 0 0 52px;
    border-right: 4px solid var(--olive-light);
  }
  .person-name { color: var(--olive-light); font-size: 24px; font-weight: 400; }
  .person-role { font-size: 17px; margin-top: 4px; }
  .contact-list { list-style: none; margin-top: 20px; }
  .contact-list li {
    display: flex; align-items: center; gap: 10px;
    font-size: 17px; line-height: 25px;
  }
  .contact-list svg { width: 16px; height: 16px; flex: none; fill: var(--olive-light); }
  .tagline { font-size: 17px; font-weight: 700; margin-top: 8px; }
  .brand-panel {
    flex: 1; display: flex; align-items: center; justify-content: center;
  }
  .brand-back {
    display: flex; align-items: center; gap: 12px;
    font-size: 25px; font-weight: 400; color: var(--ink);
  }
  .brand-back .brand-dot { background: var(--olive); width: 18px; height: 18px; }
</style>
</head>
<body>
<main class="sheet">
  <section class="card card-front" aria-label="Card front">
    <div class="brand-front"><span class="brand-dot"></span>RK Capital Stewardship</div>
    <p class="services">Alternative Investment Fund Manager &bull; Longevity Specialist &bull; Founded 1990</p>
    <div class="rule"></div>
    <p class="regulatory">RK Capital Stewardship Ltd is an Alternative Investment Fund Manager Authorised<br>and Regulated by the Monetary Oversight Bureau. Registered No. 7139604</p>
  </section>

  <section class="card card-back" aria-label="Card back">
    <div class="contact-panel">
      <h1 class="person-name">Martin Harlow</h1>
      <p class="person-role">Non-Executive Chairman</p>
      <ul class="contact-list">
        <li><svg viewBox="0 0 16 16"><path d="M1 5c0-2 2-3 7-3s7 1 7 3v1h-4V4.5H5V6H1zM3 7h10l1 7H2zM8 8.5a2.2 2.2 0 1 0 0 4.4 2.2 2.2 0 0 0 0-4.4z"/></svg>+44 (0)1632 960418</li>
        <li><svg viewBox="0 0 16 16"><path d="M4.5 0h7A1.5 1.5 0 0 1 13 1.5v13a1.5 1.5 0 0 1-1.5 1.5h-7A1.5 1.5 0 0 1 3 14.5v-13A1.5 1.5 0 0 1 4.5 0zM5 2v10h6V2zm3 11a1 1 0 1 0 0 2 1 1 0 0 0 0-2z"/></svg>+44 (0)7700 900527</li>
        <li><svg viewBox="0 0 16 16"><path d="M1 3h14v10H1zm1.5 1.2L8 8.6l5.5-4.4z"/></svg>mharlow@rkcapfold.co.uk</li>
        <li><svg viewBox="0 0 16 16"><path d="M8 0a8 8 0 1 0 0 16A8 8 0 0 0 8 0zm0 1.5c1 0 2 2.6 2.2 5.7H5.8C6 4.1 7 1.5 8 1.5zM5.8 8.8h4.4C10 11.9 9 14.5 8 14.5S6 11.9 5.8 8.8z"/></svg>www.rkcapfold.co.uk</li>
      </ul>
      <p class="tagline">Wisdom built to endure</p>
    </div>
    <div class="brand-panel">
      <div class="brand-back"><span class="brand-dot"></span>RK Capital Stewardship</div>
    </div>
  </section>
</main>
</body>
</html>
```